120ml Jar Label — Masculine Cosmetic Foot Balm for Cracked, Hardworking Heels

We need a print-ready wraparound label for a 120ml jar — a brown/amber glass jar with a black metal screw lid (file photo attached).

--DO NOT PUT A BARCODE ON THE LABEL PLEASE--
**PLEASE READ "PLAN HUDDLE PROJECT BRIEF FINAL.MD" IN ATTACHED FILES IF YOU ARE SUBMITTING A DESIGN.**

The label is 190mm wide × 40mm high.
We need files to be in an .ai format with a 2mm bleed at the end.
Social media handle: @bramblekeepnz (facebook, instagram and tiktok)

Bramble Keep is a New Zealand foot-care brand making practical, no-nonsense products for hardworking men whose jobs wreck their feet. Our flagship product, Ridge Mender Balm, helps fix thick, cracked, hardworking skin.

Brand color scheme and overview is all in the brief file. You may add some brand aligned colors outside of the specified hex codes as you see fit to make a great design. Feel free to remove the "Bramble Keep" text from the logo so Bramble Keep is not doubled up on the front of the label

The tone we want: direct, rugged, and credible — like a workwear brand, not a spa brand. Most cracked-heel products on the market lean soft and feminine; we want to stand apart by looking like a serious fix for a real problem, made in New Zealand.

Full legal requirements for New Zealand cosmetic labelling (ingredients, directions, net contents, origin, etc.) are listed in the attached brief document — these are non-negotiable and must stay legible.

Please see the label attached "Label spacing guide" for this project's rough spacing guide. This label is the same size and sits well on the jar. This label doesn't need to be spaced quite as much as the Verin Label

I want to run the design for a week - I feel 7 days is a good amount of time for designers to see the work, digest the brief and create something remarkable and memorable for Bramble Keep.

Target Market(s)

Working men in New Zealand whose jobs or lifestyle put heavy wear on their feet — tradies, farmers, hospital/shift workers, hunters, and outdoors people. Practical, value-driven buyers rather than luxury skincare shoppers.

Industry/Entity Type

Beauty / Health & Wellness / Cosmetics

Font styles to use
Sans Serif
Other font styles liked:
• Montserrat (bold, headings), Inter (regular, body)

Colors
00AB8E
00BBA5
67D7C9
C6EFE9
E9F9F6
FFC000
F8CF3A
FAE287
FDF2CF
FEFAEE

Requirements
Must have
• All NZ cosmetic labelling requirements from the attached brief (product name, tag line, net contents, ingredients, directions, storage, made in NZ) — legible and complete, not omitted for aesthetics Fits 190mm × 40mm wraparound format for a 120ml brown jar with black lid Uses our existing brand colors: Deep Olive #3C4A34, Bone White #F4EFE6, Terracotta Clay #C1683D, and Warm Grey #4A4540 (exact palette in attached brief) Uses Montserrat (headings) and Inter (body) or close equivalents Incorporates our existing shield-and-wing logo (attached) Brand name and product name clearly readable from a normal shelf/bathroom-cabinet distance
Nice to have
• A style that could extend into a hero/product photo later, similar to the NZ-hills-backdrop look on our website (screenshot attached) — not required for the label itself, just good to keep in mind Original icon work (e.g. a small soak/apply/sock icon set) if it fits the rugged brand feel A design that could work as a small back-label/wraparound split if the front can't fit everything at a readable size
Should not have
• No pastel colors, floral motifs, or delicate script fonts — this should never look like spa/luxury skincare. Don't introduce new brand colors outside the palette provided other than black.

```html
<!DOCTYPE html>
<html lang="en">
<head>
<meta charset="utf-8">
<title>Ridge Mender Balm – Jar Label</title>
<link href="https://fonts.googleapis.com/css2?family=Montserrat:wght@400;500;600;700;800&display=swap" rel="stylesheet">
<style>
  :root {
    --olive-deep: #1e3a2e;
    --olive-darker: #132a20;
    --bone: #f4efe6;
    --clay: #a86a45;
    --flag-blue: #2a2f7a;
    --page: #ffffff;
  }
  * { margin: 0; padding: 0; box-sizing: border-box; }
  html, body {
    width: 1200px; height: 390px; overflow: hidden;
    background: var(--page);
    font-family: "Montserrat", sans-serif;
    color: var(--bone);
  }
  .canvas { position: relative; width: 1200px; height: 390px; }
  .label {
    position: absolute; left: 32px; top: 71px; width: 1140px; height: 240px;
    background: linear-gradient(180deg, var(--olive-deep) 0%, var(--olive-deep) 65%, var(--olive-darker) 100%);
    box-shadow: 0 14px 14px -6px rgba(0,0,0,0.28);
    overflow: hidden;
  }
  .label > * { position: absolute; }

  .section-heading { font-weight: 700; letter-spacing: 0.6px; }

  .ingredients-heading { left: 46px; top: 52px; font-size: 8.5px; }
  .ingredients-list {
    left: 46px; top: 63px; width: 300px;
    font-size: 9px; line-height: 11px; letter-spacing: 0.35px;
  }
  .storage-heading { left: 48px; top: 129px; font-size: 8.5px; }
  .storage-text {
    left: 48px; top: 140px; width: 240px;
    font-size: 10.3px; line-height: 12px; letter-spacing: 0.4px;
  }
  .social-dot {
    width: 27px; height: 27px; border-radius: 50%; background: var(--bone); top: 179px;
  }
  .social-dot.first { left: 48px; }
  .social-dot.second { left: 83px; }
  .social-dot.third { left: 118px; }
  .social-handle { left: 160px; top: 186px; font-size: 9.6px; font-weight: 600; letter-spacing: 0.5px; }

  .divider { background: var(--bone); width: 4px; }
  .divider.left { left: 368px; top: 0; height: 161px; }
  .divider.right { left: 813px; top: 159px; height: 81px; }

  .product-name {
    left: 415px; top: 48px;
    font-size: 40px; line-height: 33px; font-weight: 700; letter-spacing: -0.3px;
  }
  .tagline {
    left: 416px; top: 163px;
    font-size: 15px; line-height: 17.5px; font-weight: 400; letter-spacing: 2.2px;
  }

  .brand-mark {
    left: 640px; top: 33px; width: 90px; height: 90px; border-radius: 50%;
    background: var(--clay); opacity: 0.9;
  }
  .brand-name {
    left: 585px; top: 147px; width: 200px; text-align: center;
    font-size: 20px; font-weight: 800; letter-spacing: 0.2px;
  }
  .brand-region {
    left: 585px; top: 171px; width: 200px; text-align: center;
    font-size: 12px; font-weight: 800;
  }
  .net-contents {
    left: 585px; top: 196px; width: 200px; text-align: center;
    font-size: 18.5px; font-weight: 500;
  }

  .directions-heading { left: 874px; top: 66px; font-size: 13.5px; letter-spacing: 2px; }
  .directions-text {
    left: 873px; top: 86px; width: 232px;
    font-size: 11.8px; line-height: 14.3px; letter-spacing: 0.5px;
  }
  .origin-flag {
    left: 874px; top: 189px; width: 43px; height: 28px; background: var(--flag-blue);
  }
  .origin-text { left: 924px; top: 196px; font-size: 13px; font-weight: 700; letter-spacing: 0.6px; }
</style>
</head>
<body>
<div class="canvas">
  <section class="label" role="img" aria-label="Deep olive label with a faint organic contour pattern">
    <h2 class="section-heading ingredients-heading">INGREDIENTS:</h2>
    <p class="ingredients-list">Shea Butter, Beef Tallow, Beeswax, Grape Seed Oil, Vegetable Glycerin, Lanolin, Propylene Glycol, Panthenol, Gluconolactone &amp; Sodium Benzoate, Manuka Honey, Allantoin, Vitamin E, Tea Tree Essential Oil, Lemon Myrtle Essential Oil, Rosemary Oleoresin Extract</p>

    <h2 class="section-heading storage-heading">STORAGE:</h2>
    <p class="storage-text">Keep out of direct sunlight. Best used within six months of opening.</p>

    <span class="social-dot first"></span>
    <span class="social-dot second"></span>
    <span class="social-dot third"></span>
    <span class="social-handle">@bramblekeepnz</span>

    <span class="divider left"></span>

    <h1 class="product-name">Ridge<br>Mender<br>Balm</h1>
    <p class="tagline">FOR<br>HARDWORKING<br>SOLES</p>

    <span class="brand-mark"></span>
    <p class="brand-name">BRAMBLE KEEP</p>
    <p class="brand-region">NZ</p>
    <p class="net-contents">120ml</p>

    <span class="divider right"></span>

    <h2 class="section-heading directions-heading">DIRECTIONS</h2>
    <p class="directions-text">Apply generously to clean, dry feet, focusing on heels and thick or cracked areas. For cracked heels, wear our moisture-locking socks overnight. Use daily.</p>

    <span class="origin-flag" role="img" aria-label="New Zealand flag"></span>
    <span class="origin-text">Made in New Zealand</span>
  </section>
</div>
</body>
</html>
```